Looking for a modern website banner design

Corvella Fieldmark Consultants looking for the development of the main banner of the website. The project description and photos are included in the upload files.

```html
<!DOCTYPE html>
<html lang="en">
<head>
<meta charset="utf-8">
<title>Corvella Fieldmark Consultants – Website Banner Concepts</title>
<link rel="stylesheet" href="https://fonts.googleapis.com/css2?family=Lato:ital,wght@0,400;0,700;1,300&display=swap">
<style>
  :root{
    --board:#dcdcde;
    --brand-blue:#0f78cc;
    --brand-blue-deep:#0b63b0;
    --stripe-grey:#9a9a9a;
    --light-bg-a:#ececed;
    --light-bg-b:#fbfbfb;
    --dark-bg:#434244;
    --ink:#2a2a2a;
    --ink-light:#ffffff;
    --caption:#777779;
  }
  *{box-sizing:border-box;margin:0;padding:0}
  html,body{width:1200px;height:1187px;overflow:hidden}
  body{background:var(--board);font-family:"Lato",sans-serif;position:relative}

  .banner{
    position:absolute;left:81px;width:1038px;height:486px;overflow:hidden;
    box-shadow:0 6px 12px rgba(0,0,0,.22);
  }
  .banner--light{top:75px;background:linear-gradient(160deg,var(--light-bg-a) 0%,var(--light-bg-b) 45%,var(--light-bg-a) 100%);color:var(--ink)}
  .banner--dark{top:589px;background:var(--dark-bg);color:var(--ink-light)}

  .banner__stripes{position:absolute;inset:0;width:1038px;height:486px}

  .brand{position:absolute;left:54px;top:46px;display:flex;align-items:center;gap:12px}
  .brand__dot{width:44px;height:44px;border-radius:50%;background:var(--brand-blue);flex:none}
  .brand__name{font-weight:700;font-size:27px;line-height:29px;color:var(--brand-blue);letter-spacing:.2px}

  .testimonial{position:absolute;left:61px;top:170px;width:500px}
  .testimonial__quote{font-style:italic;font-weight:300;font-size:22px;line-height:28.2px;letter-spacing:-.2px}
  .testimonial__author{position:absolute;left:279px;top:160px;width:260px}
  .testimonial__name{display:inline-block;font-weight:700;font-size:17.5px;color:var(--brand-blue-deep);text-transform:uppercase;letter-spacing:.2px;line-height:22px}
  .testimonial__rule{width:100px;height:2px;background:var(--brand-blue);margin:2px 0 7px}
  .testimonial__role{font-size:16px;line-height:20px}
  .banner--dark .testimonial__name{color:var(--brand-blue)}

  .athlete-photo{
    position:absolute;left:592px;top:26px;width:440px;height:460px;
    border-radius:160px 160px 0 0;
    background:linear-gradient(180deg,rgba(240,240,244,.95) 0%,rgba(226,228,236,.95) 40%,rgba(120,130,175,.9) 70%,rgba(210,80,80,.75) 100%);
  }

  .caption{position:absolute;top:1112px;left:0;width:1200px;text-align:center;font-size:17px;color:var(--caption);letter-spacing:.6px}
</style>
</head>
<body>

  <section class="banner banner--light">
    <svg class="banner__stripes" viewBox="0 0 1038 486" aria-hidden="true">
      <defs>
        <linearGradient id="greyFadeA" x1="1" y1="0" x2="0" y2="1">
          <stop offset="0" stop-color="#8e8e8e"/><stop offset="1" stop-color="#d8d8d8" stop-opacity="0"/>
        </linearGradient>
        <linearGradient id="cornerFadeA" x1="1" y1="1" x2="0" y2="0">
          <stop offset="0" stop-color="#0f78cc"/><stop offset="1" stop-color="#0f78cc" stop-opacity=".15"/>
        </linearGradient>
      </defs>
      <polygon points="799,0 873,0 660,213 586,213" fill="url(#greyFadeA)"/>
      <polygon points="935,0 1038,0 790,248 687,248" fill="#0f78cc"/>
      <polygon points="640,240 742,240 988,486 886,486" fill="url(#greyFadeA)" opacity=".6"/>
      <polygon points="730,286 833,286 1033,486 931,486" fill="#0f78cc"/>
      <polygon points="0,400 86,486 50,486 0,436" fill="url(#cornerFadeA)"/>
    </svg>

    <div class="brand">
      <span class="brand__dot"></span>
      <span class="brand__name">Corvella Fieldmark<br>Consultants</span>
    </div>

    <div class="testimonial">
      <p class="testimonial__quote">“Corvella has provided support that has allowed me to develop as a person and an athlete. The P.A.C.E.™ process allowed me to stay focused on attainable goals each season and progress from Junior to College and now Professional Hockey.”</p>
      <div class="testimonial__author">
        <span class="testimonial__name">Marcus Delane</span>
        <div class="testimonial__rule"></div>
        <p class="testimonial__role">Riverton Comets<br>Atlantic Regional Hockey League</p>
      </div>
    </div>

    <div class="athlete-photo" role="img" aria-label="Cut-out photo of a professional hockey player in a white, red and blue jersey skating with a stick"></div>
  </section>

  <section class="banner banner--dark">
    <svg class="banner__stripes" viewBox="0 0 1038 486" aria-hidden="true">
      <defs>
        <linearGradient id="greyFadeB" x1="1" y1="0" x2="0" y2="1">
          <stop offset="0" stop-color="#b0b0b0"/><stop offset="1" stop-color="#6a6a6a" stop-opacity="0"/>
        </linearGradient>
      </defs>
      <polygon points="799,0 873,0 660,213 586,213" fill="url(#greyFadeB)"/>
      <polygon points="935,0 1038,0 790,248 687,248" fill="#0f78cc"/>
      <polygon points="640,240 742,240 988,486 886,486" fill="url(#greyFadeB)" opacity=".6"/>
      <polygon points="730,286 833,286 1033,486 931,486" fill="#0f78cc"/>
      <polygon points="0,400 86,486 50,486 0,436" fill="#0f78cc"/>
    </svg>

    <div class="brand">
      <span class="brand__dot"></span>
      <span class="brand__name">Corvella Fieldmark<br>Consultants</span>
    </div>

    <div class="testimonial">
      <p class="testimonial__quote">“Corvella has provided support that has allowed me to develop as a person and an athlete. The P.A.C.E.™ process allowed me to stay focused on attainable goals each season and progress from Junior to College and now Professional Hockey.”</p>
      <div class="testimonial__author">
        <span class="testimonial__name">Marcus Delane</span>
        <div class="testimonial__rule"></div>
        <p class="testimonial__role">Riverton Comets<br>Atlantic Regional Hockey League</p>
      </div>
    </div>

    <div class="athlete-photo" role="img" aria-label="Cut-out photo of a professional hockey player in a white, red and blue jersey skating with a stick"></div>
  </section>

  <p class="caption">Design Concept 2</p>

</body>
</html>
```